Tourism Marketing needing sleek, clear design for business card & proposal documents.

***Company background***
"Quiet Harbour" is a company specializing in tourism marketing and project management. We do international wholesale, event management as well as ongoing representation of tourism and hospitality companies.

***Target market***
We cater to tourism companies and hotel professionals.

***Task***
We would like to get a single sided business card designed (but will still consider two sided, we are open to any ideas you may have). The layout for this card should be modern and elegant. Currently we do not have a logo, but we would like our business name in a really simple typography for the business card (similar to Merrow Lounge's logo - www.merrowlounge.com.au).We are after a design that is clear, strong enough to be recognised as Quiet Harbour that does not require any fancy design. Another option is a simple play on QH (Quiet Harbour) or simply have Quiet Harbour featured elsewhere on card more as a brand/logo.

Feel free to submit different fonts if you feel you have any other fonts/designs that may be suitable for this card other than sans serifs. Should this project be successful, we will be considering several other projects for business proposal templates and eventually a website design.

The information that needs to go on the card are as follows:

Odette Farrow
Director
Quiet Harbour
Tourism Marketing & Representation
57 Wendlow Terrace
Elmsbrook, Northvale, 2947 Australia
T +61 428306172 E odette@quietharbour.com.au

***Look and feel***
We'd like the business card design to express the following:
Modern, sleek, elegant, simple, discreet, quality, subtle, professional, creative, innovation

In terms of typography, we like something really simple and blocky (similar font to Merrow Lounge's logo - www.merrowlounge.com.au)

***Colour scheme***
Shades of grey and dark teal

***Note***
Although our main target market are professionals, we would like the business card design to be versatile enough to be used outside of the tourism industry and need to appeal to different markets.

I do not have existing logo. Was hoping for a design that may be clear, strong enough not to require one. Other option is a simple play on QH (Quiet Harbour) or simply have Quiet Harbour featured elsewhere on card more as a brand/logo.

Odette Farrow
Director
Quiet Harbour Pty Ltd 
57 Wendlow Terrace
T +61 428306172  E  odette@quietharbour.com.au

Thank you for designs so far. Many have used a mauve colour which matches our company profile. This is not necessary, as that is just a draft and will be completely redesigned, so dont  feel you need to incorporate the mauve.

My colour preferences are for a white or grey background, and I like fonts in dark teals, grey or other sophisticated but modern colours. feel free to submit different fonts if you you have other fonts you thing would be suitable for this card, along with sans serifs. Should this project be successful, we will be considering several others for business proposal templates and eventually website. 

Target Market(s)

International Hospitality Senior Executives, Directors of International Tourism Companies, Directors of Tourism Bodies Internationally, local Tourism

Industry/Entity Type

Hospitality

Requirements
Should not have
• must not have bright garish colour, swirly patterns or anything that dates too much.

```html
<!DOCTYPE html>
<html lang="en">
<head>
<meta charset="utf-8">
<title>Quiet Harbour — Business Card</title>
<link rel="stylesheet" href="https://fonts.googleapis.com/css2?family=Arimo:wght@400;700&family=PT+Sans:wght@400;700&display=swap">
<style>
  :root {
    --backdrop: #e6e4e1;
    --card: #ffffff;
    --card-edge: #8a8a8a;
    --ink-dark: #333333;
    --ink-mid: #555555;
    --ink-soft: #4a4a4a;
    --accent-bar: #4d4d4d;
  }
  * { margin: 0; padding: 0; box-sizing: border-box; }
  html, body { width: 1200px; height: 1063px; overflow: hidden; }
  body { background: var(--backdrop); position: relative; }

  .card {
    position: absolute;
    width: 797px;
    height: 454px;
    background: var(--card);
    border: 1px solid var(--card-edge);
    border-radius: 38px;
    overflow: hidden;
  }
  .card--front { left: 79px; top: 53px; border-color: #c9c9c9; }
  .card--back { left: 320px; top: 546px; }

  .wordmark {
    position: absolute;
    font-family: "Arimo", Arial, sans-serif;
    font-weight: 700;
    font-size: 77px;
    line-height: 1;
    letter-spacing: -0.5px;
    color: var(--ink-dark);
    white-space: nowrap;
  }
  .tagline {
    position: absolute;
    font-family: "Arimo", Arial, sans-serif;
    font-weight: 400;
    font-size: 26px;
    line-height: 1;
    letter-spacing: 1.2px;
    color: var(--ink-dark);
    white-space: nowrap;
  }

  .brand-bar {
    position: absolute;
    left: 0; top: 38px;
    width: 8px; height: 132px;
    background: var(--accent-bar);
  }
  .card--front .wordmark { left: 21px; top: 48px; }
  .card--front .tagline { left: 24px; top: 131px; }

  .contact-bar {
    position: absolute;
    right: 2px; top: 182px;
    width: 9px; height: 225px;
    background: var(--accent-bar);
  }
  .contact {
    position: absolute;
    right: 33px; top: 0;
    font-family: "PT Sans", "Myriad Pro", sans-serif;
    text-align: right;
    color: var(--ink-mid);
  }
  .contact > * { position: absolute; right: 0; white-space: nowrap; line-height: 1; }
  .contact__name { top: 192px; font-size: 23px; color: var(--ink-dark); }
  .contact__name strong { font-weight: 700; }
  .contact__name span { font-weight: 400; }
  .contact__company { top: 239px; font-size: 20px; font-weight: 700; }
  .contact__address-1 { top: 268px; font-size: 20px; }
  .contact__address-2 { top: 291px; font-size: 20px; }
  .contact__line { font-size: 19px; display: flex; align-items: center; gap: 5px; color: var(--ink-soft); }
  .contact__line svg { width: 13px; height: 13px; fill: var(--ink-soft); }
  .contact__phone { top: 332px; }
  .contact__email { top: 358px; }
  .contact__web { top: 384px; }

  .card--back .wordmark,
  .card--back .tagline,
  .card--back .web-address { left: 0; right: 0; text-align: center; }
  .card--back .wordmark { top: 150px; }
  .card--back .tagline { top: 238px; }
  .web-address {
    position: absolute;
    top: 338px;
    font-family: "PT Sans", "Myriad Pro", sans-serif;
    font-size: 19px;
    line-height: 1;
    letter-spacing: 3.2px;
    color: var(--ink-soft);
  }
</style>
</head>
<body>

  <section class="card card--front" aria-label="Business card front">
    <div class="brand-bar"></div>
    <div class="wordmark">quiet harbour</div>
    <div class="tagline">Tourism Marketing &amp; Representation</div>

    <div class="contact-bar"></div>
    <div class="contact">
      <p class="contact__name"><strong>Odette Farrow,</strong> <span>Director</span></p>
      <p class="contact__company">Quiet Harbour Pty Ltd</p>
      <p class="contact__address-1">57 Wendlow Terrace, Elmsbrook</p>
      <p class="contact__address-2">Northvale, 2947 Australia</p>
      <p class="contact__line contact__phone">+61 428306172
        <svg viewBox="0 0 16 16" aria-hidden="true"><path d="M3.5 1.5 6 4 4.7 6.2a9 9 0 0 0 5.1 5.1L12 10l2.5 2.5-1.6 2A11 11 0 0 1 1.5 3.1z"/></svg>
      </p>
      <p class="contact__line contact__email">odette@quietharbour.com.au
        <svg viewBox="0 0 16 16" aria-hidden="true"><path d="M1 4h14v9H1z M1.5 4.5 8 9l6.5-4.5" stroke="#fff" stroke-width="1"/></svg>
      </p>
      <p class="contact__line contact__web">www.Quiet Harbour.com
        <svg viewBox="0 0 16 16" aria-hidden="true"><circle cx="8" cy="8" r="7"/><path d="M1 8h14M8 1c-3 3-3 11 0 14M8 1c3 3 3 11 0 14" stroke="#fff" stroke-width="1" fill="none"/></svg>
      </p>
    </div>
  </section>

  <section class="card card--back" aria-label="Business card back">
    <div class="wordmark">quiet harbour</div>
    <div class="tagline">Tourism Marketing &amp; Representation</div>
    <div class="web-address">www.Quiet Harbour.com</div>
  </section>

</body>
</html>
```